Business Card Design Project

We need a Business Card for an Mechanical Engineering firm in Singapore. The design should be Modern & Technical looking, yet eye catching.

Our company deals in Cutting Tools & Machine Accessories for the Manufacturing Industries such as Oil & Gas, Aero Space, etc... For more information on our Company, you can either email me or view our website www.torvale.com.sg.

We are trying to revamp our image to give our consumers a fresh new perspective to our company, so we welcome all ideas.

Industry/Entity Type

Business

Requirements
Must have
• Must incorporate New Company Logo into the card as shown in Uploaded file.

```html
<!DOCTYPE html>
<html lang="en">
<head>
<meta charset="utf-8">
<title>Torvale Tools Business Card</title>
<link href="https://fonts.googleapis.com/css2?family=Arimo:wght@400;700&display=swap" rel="stylesheet">
<style>
  :root {
    --brand-red: #9e3042;
    --card-cream: #ebe7e1;
    --rule-pink: #d9aeb3;
    --text-light: #ffffff;
    --page-bg: #e4e1dc;
  }
  * { margin: 0; padding: 0; box-sizing: border-box; }
  html, body {
    width: 1200px; height: 900px; overflow: hidden;
    background: var(--page-bg);
    font-family: "Arimo", Arial, sans-serif;
  }
  .stage {
    position: relative; width: 1200px; height: 900px;
    display: flex; justify-content: center; align-items: center; gap: 120px;
  }
  .card {
    position: relative; width: 360px; height: 630px;
    background: var(--card-cream); overflow: hidden;
    box-shadow: 0 6px 18px rgba(0,0,0,0.18);
  }
  .card svg.shape { position: absolute; left: 0; width: 360px; display: block; }

  /* Front */
  .front-header {
    height: 200px; display: flex; align-items: center; justify-content: center;
    border-bottom: 6px solid var(--rule-pink);
  }
  .brand-name {
    display: flex; align-items: center; gap: 10px;
    color: var(--brand-red); font-weight: 700; font-size: 30px; letter-spacing: 1px;
  }
  .brand-dot { width: 16px; height: 16px; border-radius: 50%; background: var(--brand-red); }
  .front-body {
    position: absolute; top: 206px; left: 0; right: 0; bottom: 0;
    background: var(--brand-red); color: var(--text-light); text-align: center;
    padding-top: 34px;
  }
  .person-name {
    display: inline-block; font-weight: 700; font-size: 27px;
    padding: 0 6px 6px; border-bottom: 1.5px solid var(--text-light);
  }
  .contact-list { margin-top: 14px; font-size: 15.5px; line-height: 1.3; }
  .contact-list .last { display: inline-block; border-bottom: 1.5px solid var(--text-light); padding: 0 6px 6px; }
  .address { margin-top: 16px; font-size: 16px; font-weight: 700; line-height: 1.3; }
  .address .company { font-weight: 700; }
  .website {
    display: inline-block; margin-top: 14px; font-size: 15.5px;
    border-top: 1.5px solid var(--text-light); padding: 8px 8px 0;
  }

  /* Back */
  .back-logo {
    position: absolute; top: 250px; left: 0; right: 0;
    display: flex; justify-content: center;
  }
  .back-website {
    position: absolute; top: 500px; left: 0; right: 0; text-align: center;
    color: var(--brand-red); font-size: 15.5px;
  }
</style>
</head>
<body>
<main class="stage">
  <section class="card card-front">
    <header class="front-header">
      <div class="brand-name"><span class="brand-dot"></span>TORVALE TOOLS</div>
    </header>
    <div class="front-body">
      <h1 class="person-name">Melissa</h1>
      <p class="contact-list">
        Tel: 65-61234570<br>
        Fax: 65-61234571<br>
        <span class="last">Email: hello@torvale.com.sg</span>
      </p>
      <p class="address">
        <span class="company">Torvale Tools Pte Ltd</span><br>
        27 Kallang Crescent #03-12,<br>
        Meridian Industrial Hub,<br>
        Singapore 339410
      </p>
      <p class="website">Website: www.torvale.com.sg</p>
    </div>
    <svg class="shape" style="bottom:0" height="140" viewBox="0 0 360 140" aria-hidden="true">
      <path d="M0,140 L0,125 C60,40 220,10 360,40 L360,140 Z" fill="var(--card-cream)"/>
    </svg>
  </section>

  <section class="card card-back">
    <svg class="shape" style="top:0" height="80" viewBox="0 0 360 80" aria-hidden="true">
      <path d="M0,0 L360,0 L360,8 C260,70 110,75 0,30 Z" fill="var(--brand-red)"/>
    </svg>
    <div class="back-logo">
      <div class="brand-name"><span class="brand-dot"></span>TORVALE TOOLS</div>
    </div>
    <p class="back-website">Website: www.torvale.com.sg</p>
    <svg class="shape" style="bottom:0" height="110" viewBox="0 0 360 110" aria-hidden="true">
      <path d="M0,110 L0,100 C50,20 250,0 360,30 L360,110 Z" fill="var(--brand-red)"/>
    </svg>
  </section>
</main>
</body>
</html>
```